Larkfield Wp design

We need a wordpress design that will incorporate a professional color scheme with company logo in a clean layout. The design needs to consider that this will be developed on a responsive theme. Colors are undetermined - can use different blue or red as highlight - creative use of colors will be important. Client wants a 'modern' look.

Industry/Entity Type

It Company

Font styles to use
Serif
Sans Serif

Colors

Designer to choose colors to be used in the design.

Requirements
Must have
• - Navigation: 1) Home 2) Real Estate For Sale 3) Auctions 4) About Us 5) Selling Your Property 6) Contact Us

Site will have slideshow - 1st image is attached.
Home Page Content:
My service, experience and dedication provide motivated Sellers and Buyers with a clear marketing advantage. I know that the only way to succeed in real estate is to provide more service than you can get anywhere else. And you will get that kind of service when you work with me.
I will provide you with the personal service you deserve. Put my professional image, reputation, and business ethics to work for you.

Header will have - Logo (attached) Contact Information. 2 Real Estate listing buttons on the right for "New Listings" and "Upcoming Auctions" - similar to http://www.oakmereplots.example/home

and will have 4 call to action boxes- 1) Land 2) Residential 3) Commercial 4) Auctions

Footer will have site nav, smaller logo, and association logos (attached)
Nice to have
• use of dropdown menus

```html
<!DOCTYPE html>
<html lang="en">
<head>
<meta charset="utf-8">
<title>Larkfield Realty</title>
<link rel="stylesheet" href="https://fonts.googleapis.com/css2?family=Roboto+Condensed:wght@300;400;700&family=Roboto+Slab:wght@500&display=swap">
<style>
:root{
  --maroon:#5c1f17;
  --maroon-dark:#4a1811;
  --navy:#2f3566;
  --navy-text:#2b3160;
  --grey-panel:#f1f1f1;
  --grey-text:#a5a5a5;
  --body-text:#3a3a3a;
  --footer:#bdbdbd;
  --white:#ffffff;
}
*{box-sizing:border-box;margin:0;padding:0}
html,body{width:1016px;height:1200px;overflow:hidden}
body{position:relative;background:var(--white);font-family:"Roboto Condensed",sans-serif;color:var(--body-text)}
.abs{position:absolute}

.site-header{left:0;top:0;width:1016px;height:84px;background:var(--maroon)}
.brand{left:132px;top:12px;width:136px;height:62px;display:flex;align-items:center;gap:8px}
.brand-mark{width:14px;height:14px;border-radius:50%;background:var(--white)}
.brand-name{font-weight:700;font-size:30px;color:var(--white);letter-spacing:.5px}
.listing-btn{top:20px;height:38px;background:var(--maroon-dark);border:1px solid #6e2a20;display:flex;align-items:center;font-family:"Roboto Slab",serif;font-size:12px;color:var(--white);letter-spacing:.3px}
.listing-btn .thumb{width:40px;height:40px;margin-left:-30px;margin-right:10px;border-radius:3px}
.btn-new{left:580px;width:104px}
.btn-new .thumb{background:linear-gradient(#c82a22 0 45%,#e9e4dc 45%)}
.btn-auction{left:756px;width:132px}
.btn-auction .thumb{background:linear-gradient(135deg,#8a5a2b,#c99a5b)}

.main-nav{left:0;top:84px;width:1016px;height:29px;background:var(--navy);border-top:1px solid #454c80}
.main-nav ul{list-style:none;position:absolute;left:130px;top:0;display:flex;height:28px}
.main-nav li{height:28px;display:flex;align-items:center;justify-content:center;font-size:11px;color:var(--white);border-right:1px solid #454c80}
.main-nav li:last-child{border-right:none}

.hero{left:0;top:113px;width:1016px;height:425px;background:linear-gradient(#4f87d8 0%,#8fb6ea 30%,#7d7062 45%,#6f8e4a 70%,#4f8a2c 100%)}
.hero-arrow{top:158px}
.hero-dots{left:487px;top:469px;display:flex;gap:3px}
.hero-dots span{width:9px;height:9px;border-radius:50%;background:var(--white)}
.hero-dots span.active{background:var(--navy);border:2px solid var(--white)}

.cta{top:490px;width:185px;height:118px;background:linear-gradient(#fff,#ececec);box-shadow:0 6px 5px -3px rgba(0,0,0,.55);text-align:center}
.cta svg{margin-top:13px}
.cta h3{font-size:18px;font-weight:700;color:var(--navy-text);margin-top:2px}
.cta p{font-size:12px;color:var(--grey-text);font-weight:700;margin-top:4px}

.section-title{font-size:13px;font-weight:700;color:var(--navy-text)}
.quick-search{left:130px;top:651px;width:758px;height:91px;background:var(--grey-panel)}
.field{top:664px;height:31px;background:var(--white);border:1px solid #d6d6d6;font-size:9.5px;font-style:italic;color:#555;display:flex;align-items:center;padding-left:11px}
.field.select::after{content:"";position:absolute;right:0;top:5px;width:23px;height:19px;border-left:1px solid #cfcfcf}
.field.select .caret{position:absolute;right:8px;top:13px;width:0;height:0;border-left:4px solid transparent;border-right:4px solid transparent;border-top:5px solid var(--navy)}
.search-btn{left:797px;top:702px;width:75px;height:27px;background:var(--maroon);color:var(--white);font-size:12px;display:flex;align-items:center;justify-content:center}

.rule{left:130px;top:779px;width:757px;height:1px;background:#d9d9d9}
.welcome-text{left:130px;top:793px;width:494px;font-size:12px;line-height:19px;font-weight:400}
.welcome-text p+p{margin-top:11px}
.welcome-photo{left:642px;top:796px;width:246px;height:108px;background:linear-gradient(#8ba25e 0%,#5c6b3e 45%,#4d7a2c 100%)}

.featured-arrows{left:867px;top:927px}
.property{top:948px;width:180px}
.property .photo{height:90px}
.property .loc{margin-top:12px;font-size:12px;font-weight:700;color:var(--grey-text);display:flex;align-items:center;gap:5px}

.site-footer{left:0;top:1078px;width:1016px;height:122px;background:var(--footer)}
.badge{top:20px;height:44px;background:#2b2b2b;border-radius:2px}
.follow{right:127px;top:22px;font-size:10px;font-weight:700;color:#1f1f1f;text-align:right}
.social{display:flex;gap:5px;justify-content:flex-end;margin-top:6px}
.social span{width:18px;height:18px;border-radius:2px}
.footer-rule{left:130px;top:83px;width:758px;height:1px;background:#d0d0d0}
.copyright{left:0;top:96px;width:1016px;text-align:center;font-size:9px;font-weight:700;color:#1f1f1f}
</style>
</head>
<body>

<header class="site-header abs">
  <div class="brand abs"><span class="brand-mark"></span><span class="brand-name">Larkfield</span></div>
  <a class="listing-btn btn-new abs"><span class="thumb" role="img" aria-label="Small red-roofed house illustration"></span>NEW LISTINGS</a>
  <a class="listing-btn btn-auction abs"><span class="thumb" role="img" aria-label="Wooden auction gavel illustration"></span>UPCOMING AUCTIONS</a>
</header>

<nav class="main-nav abs">
  <ul>
    <li style="width:80px">HOME</li>
    <li style="width:172px">REAL ESTATE FOR SALE</li>
    <li style="width:116px">AUCTIONS</li>
    <li style="width:112px">ABOUT US</li>
    <li style="width:172px">SELLING YOUR PROPERTY</li>
    <li style="width:116px">CONTACT US</li>
  </ul>
</nav>

<section class="hero abs" role="img" aria-label="Large shingle-style country house with chimneys, gardens and lawn under a blue sky"></section>
<svg class="hero-arrow abs" style="left:116px" width="24" height="40" viewBox="0 0 24 40"><path d="M20 3 4 20l16 17" fill="none" stroke="#fff" stroke-width="5"/></svg>
<svg class="hero-arrow abs" style="left:882px" width="24" height="40" viewBox="0 0 24 40"><path d="M4 3l16 17L4 37" fill="none" stroke="#fff" stroke-width="5"/></svg>
<div class="hero-dots abs"><span></span><span class="active"></span><span></span><span></span></div>

<div class="cta abs" style="left:130px">
  <svg width="40" height="46" viewBox="0 0 40 46" fill="none" stroke="#2f3566" stroke-width="2.5"><path d="M20 2v42M10 4h20M4 12h32v18H4zM10 21h20M10 40h20"/></svg>
  <h3>LAND</h3><p>CONTRARY TO POPULAR BELIEF</p>
</div>
<div class="cta abs" style="left:320px">
  <svg width="44" height="46" viewBox="0 0 44 46" fill="none" stroke="#2f3566" stroke-width="2.5"><path d="M3 24 22 4l19 20M8 20v24h28V20M18 44V31h8v13"/></svg>
  <h3>RESIDENTIAL</h3><p>CONTRARY TO POPULAR BELIEF</p>
</div>
<div class="cta abs" style="left:510px">
  <svg width="40" height="50" viewBox="0 0 40 50" fill="#2f3566"><rect x="18" y="0" width="4" height="8"/><rect x="11" y="8" width="18" height="38"/><rect x="6" y="44" width="28" height="4"/><g fill="#fff"><rect x="14" y="13" width="4" height="4"/><rect x="22" y="13" width="4" height="4"/><rect x="14" y="21" width="4" height="4"/><rect x="22" y="21" width="4" height="4"/><rect x="14" y="29" width="4" height="4"/><rect x="22" y="29" width="4" height="4"/></g></svg>
  <h3>COMMERCIAL</h3><p>CONTRARY TO POPULAR BELIEF</p>
</div>
<div class="cta abs" style="left:701px">
  <svg width="46" height="48" viewBox="0 0 46 48" fill="none" stroke="#2f3566" stroke-width="2.5"><path d="M22 4 34 16l-6 6-12-12zM19 16 4 31l5 5 15-15M24 38h18v6H24z"/></svg>
  <h3>AUCTIONS</h3><p>CONTRARY TO POPULAR BELIEF</p>
</div>

<h2 class="section-title abs" style="left:128px;top:630px">QUICK SEARCH</h2>
<div class="quick-search abs"></div>
<div class="field abs" style="left:142px;width:222px">City, Country, State</div>
<div class="field select abs" style="left:376px;width:118px">Property Type<span class="caret"></span></div>
<div class="field select abs" style="left:502px;width:117px">Squar Feet<span class="caret"></span></div>
<div class="field select abs" style="left:630px;width:117px">Min Price<span class="caret"></span></div>
<div class="field select abs" style="left:755px;width:118px">Max &nbsp;Price<span class="caret"></span></div>
<div class="search-btn abs">SEARCH</div>

<h2 class="section-title abs" style="left:130px;top:762px">WELCOME TO OUR SITE</h2>
<div class="rule abs"></div>
<div class="welcome-text abs">
  <p>My service, experience and dedication provide motivated Sellers and Buyers with a clear marketing advantage. I know that the only way to succeed in real estate is to provide more service than you can get anywhere else. And you will get that kind of service when you work with me.</p>
  <p>I will provide you with the personal service you deserve. Put my professional image, reputation, and business ethics to work for you.</p>
</div>
<div class="welcome-photo abs" role="img" aria-label="Brick ranch house among tall trees with a green lawn"></div>

<h2 class="section-title abs" style="left:131px;top:927px">FEATURED PROPERIETIES</h2>
<svg class="featured-arrows abs" width="22" height="12" viewBox="0 0 22 12" fill="none" stroke="#111" stroke-width="2"><path d="M6 1 1 6l5 5M16 1l5 5-5 5"/></svg>

<div class="property abs" style="left:130px"><div class="photo" role="img" aria-label="White two-storey house with porch and trees" style="background:linear-gradient(#6f8f4a,#e8e8e4 50%,#5f7a3a)"></div><div class="loc"><svg width="8" height="11" viewBox="0 0 8 11"><path d="M4 10.5S.5 6.5.5 4a3.5 3.5 0 0 1 7 0c0 2.5-3.5 6.5-3.5 6.5z" fill="none" stroke="#6b6b6b" stroke-width="1.3"/><circle cx="4" cy="4" r="1.2" fill="#6b6b6b"/></svg>SYDNEY, AUSTRALIA</div></div>
<div class="property abs" style="left:324px"><div class="photo" role="img" aria-label="Grey and cream house with gables under a deep blue sky" style="background:linear-gradient(#1f5fc7,#8a93a6 50%,#d8d0b8 80%,#6a7a4a)"></div><div class="loc"><svg width="8" height="11" viewBox="0 0 8 11"><path d="M4 10.5S.5 6.5.5 4a3.5 3.5 0 0 1 7 0c0 2.5-3.5 6.5-3.5 6.5z" fill="none" stroke="#6b6b6b" stroke-width="1.3"/><circle cx="4" cy="4" r="1.2" fill="#6b6b6b"/></svg>DOLLAS, UK</div></div>
<div class="property abs" style="left:517px"><div class="photo" role="img" aria-label="Large stone suburban home with landscaped garden" style="background:linear-gradient(#4c8fe0,#cfd8e0 45%,#b7a890 65%,#5e8a3a)"></div><div class="loc"><svg width="8" height="11" viewBox="0 0 8 11"><path d="M4 10.5S.5 6.5.5 4a3.5 3.5 0 0 1 7 0c0 2.5-3.5 6.5-3.5 6.5z" fill="none" stroke="#6b6b6b" stroke-width="1.3"/><circle cx="4" cy="4" r="1.2" fill="#6b6b6b"/></svg>SYDNEY, AUSTRALIA</div></div>
<div class="property abs" style="left:708px"><div class="photo" role="img" aria-label="House with three dormer windows and flowering porch" style="background:linear-gradient(#5a9ae0,#6a6e78 40%,#e6e6e0 65%,#4f7a32)"></div><div class="loc"><svg width="8" height="11" viewBox="0 0 8 11"><path d="M4 10.5S.5 6.5.5 4a3.5 3.5 0 0 1 7 0c0 2.5-3.5 6.5-3.5 6.5z" fill="none" stroke="#6b6b6b" stroke-width="1.3"/><circle cx="4" cy="4" r="1.2" fill="#6b6b6b"/></svg>DOLLAS, UK</div></div>

<footer class="site-footer abs">
  <div class="badge abs" style="left:130px;width:40px"></div>
  <div class="badge abs" style="left:184px;width:84px;height:40px;top:22px"></div>
  <div class="badge abs" style="left:282px;width:34px"></div>
  <div class="badge abs" style="left:338px;width:38px;height:40px"></div>
  <div class="follow abs">FOLLOW US ON
    <div class="social"><span style="background:#3b5998"></span><span style="background:#1a78b4"></span><span style="background:#39a9e0"></span><span style="background:#f08a1c"></span></div>
  </div>
  <div class="footer-rule abs"></div>
  <div class="copyright abs">COPYRIGHTS @ 2014 ALL RIGHTS RESERVED</div>
</footer>

</body>
</html>
```